Agricultural Consulting Website

Provide a modern yet business like website for my new Agriculture Consulting Business in Australia called FieldNorth. Whilst we are based in Australia we are targetting both domestic and international markets (especially in Asia). We are targetting corporate, small business, government and farmer clients. The design should compliment our logo also sourced through pixel harbor. The webiste should be easy for me to keep updated on a regular basis without the need to go back to the designer.

Industry/Entity Type

Business

Requirements
Must have
• clean crisp feel
• be modern yet business like
• be able to be updated by myself easily

```html
<!DOCTYPE html>
<html lang="en">
<head>
<meta charset="utf-8">
<title>FieldNorth – Agricultural Consultancy</title>
<link rel="stylesheet" href="https://fonts.googleapis.com/css2?family=Arimo:wght@400;700&family=Didact+Gothic&family=Open+Sans:wght@700&display=swap">
<style>
:root{
  --green:#5e9a0b;
  --brown:#5a3309;
  --text:#555555;
  --dark:#333333;
  --grey-btn:#666666;
  --panel:#f4f4f4;
  --footer:#313131;
  --white:#ffffff;
}
*{margin:0;padding:0;box-sizing:border-box}
html,body{width:1165px;height:1200px;overflow:hidden;background:var(--white)}
body{position:relative;font-family:"Arimo",Arial,sans-serif;color:var(--text)}
.site-header{position:absolute;left:0;top:0;width:1165px;height:91px}
.brand{position:absolute;left:146px;top:16px;height:59px;display:flex;align-items:center;gap:10px}
.brand-mark{width:48px;height:48px;background:var(--green)}
.brand-name{font-family:"Didact Gothic",sans-serif;font-size:36px;color:var(--green)}
.main-nav{position:absolute;top:39px;left:563px;display:flex;font-size:13px}
.main-nav a{display:block;height:26px;line-height:26px;color:var(--dark);text-decoration:none;padding:0 18px}
.main-nav a.active{background:var(--green);color:var(--white)}
.hero{position:absolute;left:0;top:91px;width:1165px;height:415px;
  background:linear-gradient(180deg,#9cc0dc 0%,#c9d9c4 14%,#a9a553 24%,#8c9a3a 32%,#3f7a14 46%,#5a9a1c 70%,#3f7b16 100%)}
.hero-title{position:absolute;left:0;width:100%;top:183px;text-align:center;color:var(--white)}
.hero-title .line1{display:block;font-family:"Didact Gothic",sans-serif;font-size:46px;line-height:48px}
.hero-title .line2{display:block;font-family:"Open Sans",sans-serif;font-weight:700;font-size:33px;line-height:36px}
.hero-arrow{position:absolute;top:177px}
.services{position:absolute;left:146px;top:540px;width:874px;display:flex;justify-content:space-between}
.service{width:200px}
.service h2{font-family:"Didact Gothic",sans-serif;font-weight:400;font-size:21px;color:var(--green);height:34px;white-space:nowrap}
.service .thumb{width:200px;height:107px;border:3px solid #dcdcdc}
.service p{margin-top:18px;font-size:11px;line-height:14.5px;text-align:justify;height:72px}
.btn{display:inline-block;width:75px;height:25px;line-height:25px;text-align:center;font-size:12px;color:var(--white);background:var(--grey-btn);text-decoration:none}
.btn.is-green{background:var(--green)}
.about{position:absolute;left:146px;top:850px;width:620px}
.about h1{font-family:"Didact Gothic",sans-serif;font-weight:400;font-size:24px;color:var(--brown);margin-bottom:14px}
.about h1 span{color:var(--green)}
.about p{font-size:12.5px;line-height:15.5px;margin-bottom:15px}
.contact{position:absolute;left:819px;top:855px;width:200px;height:238px;background:var(--panel);padding:10px 14px}
.contact h3{font-family:"Didact Gothic",sans-serif;font-weight:400;font-size:20px;color:var(--brown);padding-bottom:5px;border-bottom:1px solid #cccccc}
.contact .lead{margin-top:9px;font-size:12.5px;line-height:15.5px;color:#000;text-align:justify}
.contact ul{list-style:none;margin-top:12px}
.contact li{display:flex;align-items:center;gap:10px;height:29px;font-size:12.5px;color:var(--text)}
.social-btn{display:block;margin:7px 0 0 6px;width:140px;height:43px;border:1px solid #cfcfcf;background:var(--white);font-size:14px;font-weight:700;color:#3b5998;text-align:center;line-height:41px;text-decoration:none}
.site-footer{position:absolute;left:0;top:1142px;width:1165px;height:58px;border-top:5px solid var(--green);background:var(--footer);color:var(--white);font-size:11px;text-align:center;line-height:53px}
</style>
</head>
<body>
<header class="site-header">
  <div class="brand"><span class="brand-mark"></span><span class="brand-name">FieldNorth</span></div>
  <nav class="main-nav">
    <a class="active" href="#">Home</a><a href="#">About us</a><a href="#">Services</a><a href="#">News &amp; Events</a><a href="#">Contact us</a>
  </nav>
</header>

<section class="hero" role="img" aria-label="Rolling green hills above rows of young crops under a blue sky">
  <svg class="hero-arrow" style="left:68px" width="34" height="62" viewBox="0 0 34 62"><polyline points="32,1 2,31 32,61" fill="none" stroke="#fff" stroke-width="2"/></svg>
  <div class="hero-title"><span class="line1">Your Farm Profit</span><span class="line2">is Our Priority</span></div>
  <svg class="hero-arrow" style="left:1065px" width="34" height="62" viewBox="0 0 34 62"><polyline points="2,1 32,31 2,61" fill="none" stroke="#fff" stroke-width="2"/></svg>
</section>

<section class="services">
  <article class="service">
    <h2>Farm Management</h2>
    <div class="thumb" role="img" aria-label="Hay bales in a harvested field" style="background:linear-gradient(180deg,#6e9a3c 0%,#c9a466 25%,#b58c4f 100%)"></div>
    <p>Lorem ipsum dolor sit amet, consectetur adipiscing elit. Morbi vitae justo malesuada, posuere erat sit amet, mollis lacus.</p>
    <a class="btn" href="#">Read More</a>
  </article>
  <article class="service">
    <h2>Grain Marketing</h2>
    <div class="thumb" role="img" aria-label="Close view of ripe wheat ears" style="background:linear-gradient(135deg,#f0c460 0%,#c8892a 55%,#e7a83e 100%)"></div>
    <p>Lorem ipsum dolor sit amet, consectetur adipiscing elit. Morbi vitae justo malesuada, posuere erat sit amet, mollis lacus.</p>
    <a class="btn is-green" href="#">Read More</a>
  </article>
  <article class="service">
    <h2>Agronomy</h2>
    <div class="thumb" role="img" aria-label="Long rows of green crop plants" style="background:linear-gradient(180deg,#7fa85a 0%,#3c7b1e 45%,#2f5a18 100%)"></div>
    <p>Lorem ipsum dolor sit amet, consectetur adipiscing elit. Morbi vitae justo malesuada, posuere erat sit amet, mollis lacus.</p>
    <a class="btn" href="#">Read More</a>
  </article>
  <article class="service">
    <h2>Project Management</h2>
    <div class="thumb" role="img" aria-label="Two consultants reviewing notes in a crop field" style="background:linear-gradient(180deg,#8fb2d6 0%,#a7bfcf 35%,#4d7f3a 65%,#3e6b2c 100%)"></div>
    <p>Lorem ipsum dolor sit amet, consectetur adipiscing elit. Morbi vitae justo malesuada, posuere erat sit amet, mollis lacus.</p>
    <a class="btn" href="#">Read More</a>
  </article>
</section>

<section class="about">
  <h1><span>FieldNorth</span> Agricultural Consultancy</h1>
  <p>Lorem ipsum dolor sit amet, consectetur adipiscing elit. Morbi vitae justo malesuada, posuere erat sit amet, mollis lacus. Sed commodo ligula eget pretium dapibus. Suspendisse id nisi sed libero ultricies iaculis. Vestibulum turpis turpis, ultrices a eros ut, ullamcorper rhoncus tellus.</p>
  <p>Nulla eget consequat eros. Donec metus diam, mattis quis mattis elementum, eleifend sit amet est. Nunc scelerisque congue nulla, eu aliquam risus consectetur ac. Donec a accumsan felis. Proin nunc sem, ultricies ac diam a, ultrices tristique lorem. Pellentesque quis dapibus purus.</p>
  <p>Donec massa odio, porttitor molestie scelerisque et, pulvinar a odio. Pellentesque eros massa, ultricies in libero quis, feugiat ullamcorper risus.</p>
</section>

<aside class="contact">
  <h3>Contact us</h3>
  <p class="lead">Lorem ipsum dolor sit amet, consectetur adipiscing elit.</p>
  <ul>
    <li><svg width="14" height="16" viewBox="0 0 14 16"><path d="M3 1 L6 1 L6 5 L4 6 Q5 10 8 12 L10 10 L13 12 L12 15 Q4 14 2 4 Z" fill="#6b3b0c"/></svg>1800 555 019</li>
    <li><svg width="14" height="10" viewBox="0 0 14 10"><rect x="0.5" y="0.5" width="13" height="9" fill="#6b3b0c"/><polyline points="1,1 7,6 13,1" fill="none" stroke="#f4f4f4" stroke-width="1"/></svg>info@fieldnorth.com.au</li>
    <li><svg width="14" height="14" viewBox="0 0 14 14"><g fill="none" stroke="#8a5a2a" stroke-width="1"><circle cx="7" cy="7" r="6"/><ellipse cx="7" cy="7" rx="2.5" ry="6"/><line x1="1" y1="7" x2="13" y2="7"/></g></svg>www.fieldnorth.com.au</li>
  </ul>
  <a class="social-btn" href="#">Find us on Friendspace</a>
</aside>

<footer class="site-footer">Copyright © 2013 FieldNorth. All Rights Reserved.</footer>
</body>
</html>
```